Front & Back Book Cover Design

Title:
THE QUIET LANDLORD: How to Grow Comfort and Plenty Through Property Held by Others
Author:
Mel T. Varnak
Design Philosophy:
A modern, minimalist-luxury aesthetic that feels visionary and intelligent — positioned between business innovation (The Brisk Venture), modern finance (The Anatomy of Thrift), and timeless real estate insight (Bold Aunt Meek Aunt).
Think: clean, bold, and idea-driven — a visual reflection of the book’s central concept: wealth through clarity, not clutter.
Back Cover:
To include book description along with author photo and bio
Files:
PNG, PDF, EPUB

```html
<!DOCTYPE html>
<html lang="en">
<head>
<meta charset="utf-8">
<title>The Quiet Landlord — Mel T. Varnak</title>
<link rel="stylesheet" href="https://fonts.googleapis.com/css2?family=Poppins:wght@400;500;700;800&display=swap">
<style>
  :root {
    --ink: #0f0f0f;
    --paper: #ffffff;
    --text-dark: #111111;
    --portrait-light: #3a3a3a;
    --portrait-dark: #161616;
  }
  html, body {
    margin: 0;
    padding: 0;
    width: 800px;
    height: 1200px;
    overflow: hidden;
    background: var(--ink);
  }
  .cover {
    position: relative;
    width: 800px;
    height: 1200px;
    background: var(--ink);
    font-family: "Poppins", sans-serif;
    overflow: hidden;
  }
  .title-block {
    position: absolute;
    left: 0;
    top: 0;
    width: 800px;
    height: 360px;
  }
  .title-block text {
    font-family: "Poppins", sans-serif;
    font-weight: 700;
    fill: var(--paper);
  }
  .subtitle-band {
    position: absolute;
    left: 0;
    top: 428px;
    width: 800px;
    height: 169px;
    background: var(--paper);
  }
  .subtitle {
    position: absolute;
    left: 36px;
    top: 437px;
    margin: 0;
    font-size: 33px;
    line-height: 45px;
    font-weight: 400;
    color: var(--text-dark);
    letter-spacing: -0.3px;
  }
  .subtitle strong { font-weight: 700; }
  .author-portrait {
    position: absolute;
    left: 545px;
    top: 345px;
    width: 255px;
    height: 855px;
    border-radius: 120px 120px 0 0;
    background: linear-gradient(180deg, var(--portrait-light) 0%, var(--portrait-dark) 40%, #1c1c1c 70%, var(--portrait-light) 100%);
  }
  .author-name {
    position: absolute;
    left: 55px;
    top: 962px;
    margin: 0;
    font-size: 62px;
    line-height: 76px;
    font-weight: 700;
    color: var(--paper);
    letter-spacing: -1px;
    text-transform: uppercase;
  }
</style>
</head>
<body>
<main class="cover">
  <svg class="title-block" viewBox="0 0 800 360" role="heading" aria-level="1" aria-label="The Quiet Landlord">
    <text x="44" y="200" font-size="52">the</text>
    <text x="150" y="204" font-size="150" letter-spacing="-2">quiet</text>
    <text x="42" y="328" font-size="124" letter-spacing="-2" textLength="716" lengthAdjust="spacingAndGlyphs">landlord</text>
  </svg>

  <div class="subtitle-band"></div>
  <p class="subtitle">How to Grow <strong>Comfort</strong><br>and <strong>Plenty</strong> Through<br><strong>Property</strong> Held by <strong>Others</strong></p>

  <div class="author-portrait" role="img" aria-label="Portrait photograph of the author in a dark blazer over a white T-shirt"></div>

  <h2 class="author-name">Mel T.<br>Varnak</h2>
</main>
</body>
</html>
```